BPL its me again- No TIME

I am a weight loss consultant who my target audience now is staff- teachers at work.

I am Bright Path Living and I have partner up with the program Vital Kickoff. I am selling my services but it will be attached to his brochure which I attached to show you.

This flyer will be given to teachers while at work or left on the staff room lunch table.

Please make it short, snappy and fun.
Why lose weight at work? People are time poor

points:-
- Mobile weight loss consultant who comes to you at work
before/after school or lunch break.
-20 minute private 1 on 1 consultations
-limited spots (3 per hour)
-no contract
-10 years experience

If possible I would like it at work flyer for different companies as well like banks but teachers/schools are my main target.

Like the picture with the teacher in front of the board but can remove the heart if possible
Thank you

i will brochure soon to show you

Target Market(s)

people at work- during lunch breaks or before and after
First is school teachers then other companies.
Females are the majority of clients

Industry/Entity Type

Teacher

Requirements
Must have
• leave it up to you just want to grab staff's attention.
Should not have
• please never use the word "diet" its a healthy lifestyle.

```html
<!DOCTYPE html>
<html lang="en">
<head>
<meta charset="utf-8">
<title>Bright Path Living – Lose Weight at Work</title>
<link href="https://fonts.googleapis.com/css2?family=Montserrat:wght@700&family=Arimo&family=Roboto+Slab:wght@400&family=Questrial&family=Open+Sans:wght@600&display=swap" rel="stylesheet">
<style>
:root{
  --pink:#e8135a;
  --orange:#f7a21c;
  --peach:#fccb9b;
  --yellow:#fbf56a;
  --blue:#6b9cf0;
  --ink:#1d1d1d;
  --grey:#b8b8b8;
  --white:#ffffff;
}
*{margin:0;padding:0;box-sizing:border-box}
html,body{width:928px;height:1200px;overflow:hidden;background:#f2f2f2}
.flyer{position:relative;width:928px;height:1200px;background:var(--white);overflow:hidden}
.header-art{position:absolute;left:0;top:0}
.heart{position:absolute;left:24px;top:112px;width:200px;height:180px}
.heart-text{position:absolute;left:42px;top:162px;width:160px;text-align:center;transform:rotate(5deg);
  font-family:"Open Sans",sans-serif;font-weight:600;font-size:21px;line-height:27px;color:var(--white);letter-spacing:.5px}
.brand-mark{position:absolute;font-family:"Montserrat",sans-serif;font-weight:700;color:var(--white);text-align:center}
.brand-mark.top{left:560px;top:72px;width:330px;font-size:28px}
.brand-mark.faint{left:555px;top:770px;width:330px;font-size:28px;color:var(--pink);opacity:.18}
.question{position:absolute;left:660px;top:300px;font-family:"Montserrat",sans-serif;font-weight:700;font-size:260px;color:var(--grey);line-height:1}
.headline{position:absolute;left:36px;top:490px;font-family:"Montserrat",sans-serif;font-weight:700;font-size:47px;line-height:62px;color:var(--ink)}
.headline .accent,.headline .sub{color:var(--blue)}
.points{position:absolute;left:36px;top:630px;list-style:none;font-family:"Arimo",sans-serif;font-size:25px;line-height:40px;color:var(--ink)}
.points li{position:relative;padding-left:55px}
.points li::before{content:"";position:absolute;left:14px;top:13px;width:15px;height:15px;border-radius:50%;border:4px solid var(--pink)}
.cta-band{position:absolute;left:0;top:873px;width:928px;height:164px;background:var(--yellow)}
.cta-band svg{position:absolute;left:330px;top:0}
.cta-title{position:absolute;left:50px;top:906px;width:320px;text-align:center;font-family:"Roboto Slab",serif;font-size:41px;line-height:50px;color:var(--pink)}
.call-button{position:absolute;left:524px;top:914px;width:392px;height:94px;border-radius:12px;background:var(--pink);box-shadow:2px 3px 4px rgba(0,0,0,.25);
  text-align:center;color:var(--white);font-family:"Roboto Slab",serif}
.call-button .label{display:block;font-size:25px;margin-top:12px}
.call-button .number{display:block;font-size:33px;margin-top:2px}
.footer{position:absolute;left:0;top:1037px;width:928px;height:163px;background:var(--peach)}
.footer svg{position:absolute;left:0;top:0}
.program-name{position:absolute;left:30px;top:1110px;font-family:"Montserrat",sans-serif;font-weight:700;font-size:38px;color:var(--white)}
.credits{position:absolute;left:490px;top:1050px;width:430px;text-align:center;font-family:"Questrial",sans-serif;font-size:18.5px;line-height:22px;color:var(--ink)}
.credits .contact{font-weight:700;font-family:"Arimo",sans-serif}
.credits .row{display:inline-flex;align-items:center;gap:6px}
.icon{display:inline-block;width:20px;height:20px;border-radius:50%;border:2px solid var(--pink);color:var(--pink);font-size:12px;line-height:16px;text-align:center;font-weight:700}
</style>
</head>
<body>
<main class="flyer">
  <svg class="header-art" width="928" height="520" viewBox="0 0 928 520">
    <defs>
      <linearGradient id="photoTone" x1="0" y1="0" x2="1" y2="1">
        <stop offset="0" stop-color="#e9d2bd"/>
        <stop offset=".45" stop-color="#6d6f78"/>
        <stop offset=".8" stop-color="#c9a58a"/>
        <stop offset="1" stop-color="#b85a4a"/>
      </linearGradient>
      <linearGradient id="swoosh" x1="0" y1="0" x2="1" y2="0">
        <stop offset="0" stop-color="var(--pink)"/>
        <stop offset=".6" stop-color="#ef3c4a"/>
        <stop offset="1" stop-color="var(--orange)"/>
      </linearGradient>
    </defs>
    <path role="img" aria-label="Photo of a worker at a laptop picking fresh salad and tomatoes from a lunch box" fill="url(#photoTone)"
      d="M0 0H430C500 120 640 230 928 250V285C760 330 560 440 0 440Z"/>
    <path fill="var(--orange)" d="M420 0H928V268C650 250 505 140 420 0Z"/>
    <path fill="var(--pink)" d="M430 0H928V245C660 228 515 125 430 0Z"/>
    <path fill="url(#swoosh)" d="M0 430C560 440 760 320 928 270V295C760 365 560 470 0 480Z"/>
    <path fill="var(--orange)" d="M0 478C560 470 760 365 928 293V300C760 375 560 485 0 492Z"/>
  </svg>

  <svg class="heart" viewBox="0 0 200 180" aria-hidden="true">
    <path fill="var(--pink)" d="M100 176C60 140 8 110 6 60C4 22 40 2 70 12C88 18 96 30 100 42C106 28 118 14 140 12C172 8 198 34 192 72C186 116 136 140 100 176Z"/>
  </svg>
  <p class="heart-text">LOVE YOUR METABOLISM</p>

  <p class="brand-mark top">Bright Path Living</p>

  <div class="question" aria-hidden="true">?</div>

  <h1 class="headline">Why <span class="accent">lose weight</span> at work?<br><span class="sub">People are time poor</span></h1>

  <p class="brand-mark faint">Bright Path Living</p>

  <ul class="points">
    <li>Mobile weight loss consultant who comes to you at work<br>before/after school or lunch break.</li>
    <li>20 minute private 1 on 1 Consultations</li>
    <li>Limited Spots (3 per hour)</li>
    <li>No Contract</li>
    <li>10 Years Experience</li>
  </ul>

  <section class="cta-band">
    <svg width="300" height="164" viewBox="0 0 300 164" aria-hidden="true">
      <path fill="var(--white)" d="M230 0L130 70H160L40 160L200 60H170L260 0Z" opacity=".9"/>
    </svg>
  </section>
  <h2 class="cta-title">Get In Touch<br>Today</h2>
  <div class="call-button"><span class="label">Call Us Today</span><span class="number">(02) 5550 0142</span></div>

  <footer class="footer">
    <svg width="928" height="163" viewBox="0 0 928 163" aria-hidden="true">
      <path fill="var(--orange)" d="M0 -4C220 -12 420 30 510 163H495C400 40 220 2 0 6Z"/>
      <path fill="var(--pink)" d="M0 6C220 2 400 40 495 163H0Z"/>
    </svg>
  </footer>
  <p class="program-name">Vital Kickoff</p>
  <div class="credits">
    Vital Kickoff is designed by<br>
    Sam Carter &amp; Brightform Pty Ltd<br>
    ABN 12345678901, PO BOX 512<br>
    Maple Grove NSW 2000<br>
    <span class="row contact"><span class="icon">✆</span>Call: (02) 5550 0142</span><br>
    <span class="row"><span class="icon">e</span>team@vitalkickoff.com</span>
  </div>
</main>
</body>
</html>
```